依頼概要
■依頼の目的/概要
遊技業組合のポスターデザインの制作をお願いします。
パチンコ店の出玉を換金せずにお楽しみ袋と交換して家に持ち帰ってもらうよう呼びかけるポスターです。。
カウンター前にお楽しみ袋が積まれたワゴンを設置(添付PDF)
店内にポスターを貼ります。

■依頼詳細
過去の制作は26年1月はポスター。26年12月はPOPスタンドパネル。27年はのぼり、昨年28年12月はポスターを制作。
http://www.hanamizu-kumiai.jp/event/index.cgi

・パチンコ・スロットのホール内に掲示します。
・ホール内で目につくカラー・デザインをお願いします。
・社会を風刺作品や今年の流行をとり入れていただくなど。

■原稿内容
・カラー B2ポスター
・景品持ち帰り推進運動
・平成29年12月16日(土)~平成29年1月24日(日)
・山並遊興事業協同組合
コピーはお任せいたします。

その他何かご不明な点がございましたら、お気軽にご質問下さい。
よろしくお願いいたします。
■ 選んだ理由

大変お待たせしました。
どのデザインも好評でしたが目に留まることで選ばれました。
ありがとうございました。 森下

■ 提案者全員のお礼・コメント

たくさんの提案ありがとうございました。
ありがとうございました。 森下

```html
<!DOCTYPE html>
<html lang="ja">
<head>
<meta charset="utf-8">
<title>景品持ち帰り推進運動 ポスター</title>
<link rel="stylesheet" href="https://fonts.googleapis.com/css2?family=Dela+Gothic+One&family=M+PLUS+Rounded+1c:wght@700;800;900&display=swap">
<style>
:root{
  --paper:#ffffff;
  --ink:#111111;
  --navy:#1b2a6b;
  --badge:#2e8fd6;
  --sun:#fff03a;
  --magenta:#e4177a;
  --red:#e60012;
  --girl-a:#f4b3c4;
  --girl-b:#f7d7a4;
  --family-a:#c9c9c9;
  --family-b:#f1a1a8;
  --bag:#d8b46a;
}
*{margin:0;padding:0;box-sizing:border-box}
html,body{width:871px;height:1200px;overflow:hidden;background:var(--paper)}
.poster{position:relative;width:871px;height:1200px;overflow:hidden;background:var(--paper);border:8px solid var(--red);font-family:"M PLUS Rounded 1c",sans-serif;color:var(--ink)}

.headline-sun{position:absolute;left:192px;top:-38px;width:340px;height:340px;border-radius:50%;background:var(--sun)}

.period-badge{position:absolute;left:2px;top:-2px;width:230px;height:215px;border-radius:50%;background:var(--badge);color:#fff;text-align:center;padding-top:38px}
.period-badge .from{font-size:12px;font-weight:700}
.period-badge .era{font-size:25px;font-weight:900;margin-top:2px;line-height:1.2}
.period-badge .end{font-family:"Dela Gothic One",sans-serif;font-size:50px;line-height:1.1;color:var(--navy);display:flex;justify-content:center;align-items:center;gap:4px}
.period-badge .end .day{display:inline-flex;width:32px;height:32px;border-radius:50%;background:var(--red);color:#fff;font-size:20px;align-items:center;justify-content:center}
.period-badge .until{font-size:26px;font-weight:900;line-height:1.2}

.campaign-title{position:absolute;left:212px;top:30px;width:300px;text-align:center;font-family:"M PLUS Rounded 1c",sans-serif;font-weight:900;line-height:1.12}
.campaign-title .main{display:block;font-size:70px;color:var(--magenta)}
.campaign-title .sub{display:block;font-size:48px;color:var(--navy);margin-top:4px}

.girl-art{position:absolute;left:390px;top:250px;width:150px;height:110px;border-radius:40%;background:radial-gradient(circle at 50% 40%,var(--girl-b),var(--girl-a))}
.girl-bubble{position:absolute;left:552px;top:258px;width:110px;font-size:19px;font-weight:800;line-height:1.25;transform:rotate(-6deg)}

.copy-main{position:absolute;right:22px;top:30px;writing-mode:vertical-rl;font-family:"Dela Gothic One",sans-serif;font-size:160px;line-height:1;color:var(--ink)}
.copy-lead{position:absolute;left:338px;top:368px;font-size:44px;font-weight:900;line-height:1}
.copy-punch{position:absolute;left:52px;top:340px;writing-mode:vertical-rl;font-family:"Dela Gothic One",sans-serif;font-size:160px;line-height:1;color:var(--ink)}

.family-art{position:absolute;left:240px;top:430px;width:360px;height:690px;border-radius:45% 45% 10% 10%;background:linear-gradient(90deg,var(--family-a) 0%,var(--family-a) 45%,var(--family-b) 70%,var(--family-b) 100%)}
.bag-art{position:absolute;left:640px;top:1000px;width:130px;height:100px;border-radius:10px;background:linear-gradient(160deg,#f3e2b0,var(--bag))}

.organizer{position:absolute;right:52px;bottom:22px;font-size:30px;font-weight:900;letter-spacing:1px;line-height:1.2}
</style>
</head>
<body>
<main class="poster">
  <div class="headline-sun"></div>

  <div class="period-badge">
    <p class="from">平成29年12月16日(土)～</p>
    <p class="era">平成30年</p>
    <p class="end">1/24<span class="day">日</span></p>
    <p class="until">まで</p>
  </div>

  <h1 class="campaign-title">
    <span class="main">景品</span>
    <span class="main">持ち帰り</span>
    <span class="sub">推進運動</span>
  </h1>

  <div class="girl-art" role="img" aria-label="プレゼントを抱えて喜ぶ女の子のイラスト"></div>
  <p class="girl-bubble">パパ、<br>おみやげ<br>ありがと！</p>

  <p class="copy-main">そんとくより</p>
  <p class="copy-lead">たまには</p>
  <p class="copy-punch">そんたく。</p>

  <div class="family-art" role="img" aria-label="怒った母親と子ども、うなだれる父親の家族のイラスト"></div>
  <div class="bag-art" role="img" aria-label="お菓子の詰まったお楽しみ袋のイラスト"></div>

  <p class="organizer">山並遊興事業協同組合</p>
</main>
</body>
</html>
```